Brochure for Specialist Divorce Support

1. I want an A4 three fold brochure or DL to promote my business and services.
My market are people going through divorce and are usually feeling very overwhelmed and therefore not functioning very well - both men and women, age early forties,
2. Colours – variety of blues and lime greens but you choose if you need a contrast e.g. orange
3. Images – happy single families
4. Theme - could you make it around water please - soothing
5. Logos – HWN &; HWT (I will attach)
6. I have a lot of content so maybe not too busy but still professional feel +
warm and reassuring
7. I'm attaching -

- a draft brochure I put together using a Microsoft template
- a word document with extra details
- plus two logos to do with my qualifications
- and some images for you to choose from

7. I want to use this as a template for some other brochures -> more work for
the winner.

Target Market(s)

Men and women usually in their early forties with primary school aged children i.e 5 to 12 years old.
They are going through a divorce and very upset, Maybe losing contact with their children and their way of life as they know it is disappearing. They are in turmoil and not functioning as well as they usually do.

Industry/Entity Type

Business

Font styles to use
Sans Serif

Colors
34a7d7
abd037
3277b5

Requirements
Must have
• I want the brochure to be three folds with the center the full A4
• Could you make the theme around water please.
• I will upload some photos for you to use if you want,

```html
<!DOCTYPE html>
<html lang="en">
<head>
<meta charset="utf-8">
<title>Divorce Coaching – Inside Spread</title>
<link href="https://fonts.googleapis.com/css2?family=Barlow:ital,wght@0,400;0,500;0,600;0,700;1,500;1,600&display=swap" rel="stylesheet">
<style>
  :root {
    --deep-teal: #0f4e66;
    --heading-teal: #1f5e80;
    --stage-blue: #3f6fb3;
    --rule-violet: #5b5fae;
    --quote-violet: #545489;
    --fold-pink: #d0409a;
    --band-grey: #dde0e7;
    --text: #2b2b2b;
    --white: #ffffff;
  }
  * { box-sizing: border-box; margin: 0; padding: 0; }
  html, body { width: 1200px; height: 849px; overflow: hidden; background: #fff; }
  body { font-family: "Barlow", "Helvetica Neue", Arial, sans-serif; color: var(--text); }
  .spread { position: relative; width: 1200px; height: 849px; overflow: hidden; }
  .abs { position: absolute; }

  .photo-family-beach { left: 0; top: 0; width: 399px; height: 265px;
    background: linear-gradient(180deg, #8fa8b5 0%, #b9c2c2 35%, #d8c7ae 70%, #c9b493 100%); }
  .photo-beach-wash { left: 0; top: 265px; width: 800px; height: 584px;
    background: linear-gradient(180deg, #e9ecf1 0%, #dfe5ec 45%, #d2dbe4 70%, #e3e2e0 100%); }
  .photo-mother-son { left: 800px; top: 342px; width: 400px; height: 281px;
    background: linear-gradient(160deg, #c6d48a 0%, #9fb75a 45%, #7f9a3e 75%, #b4a178 100%); }

  .tagline-block { left: 399px; top: 0; width: 401px; height: 265px; background: var(--deep-teal); }
  .tagline-block .rule { position: absolute; left: 43px; width: 318px; height: 4px; background: var(--rule-violet); }
  .tagline-block .rule.top { top: 73px; }
  .tagline-block .rule.bottom { top: 185px; }
  .tagline { position: absolute; left: 50px; top: 92px; width: 300px; color: var(--white);
    font-style: italic; font-weight: 600; font-size: 12.5px; line-height: 1.3; }

  .fold { top: 0; width: 1px; height: 849px; background: var(--fold-pink); }

  .stage-num { width: 38px; background: var(--stage-blue); color: var(--white);
    font-weight: 700; font-size: 18px; padding: 8px 0 0 0; text-align: center; }
  .stage-title { color: var(--heading-teal); font-weight: 700; font-size: 18px; line-height: 1.3; }
  .body-copy { font-size: 12px; line-height: 1.32; }
  .body-copy p + p { margin-top: 2px; }

  ul.points { list-style: none; }
  ul.points li { position: relative; padding-left: 16px; margin-bottom: 3px; }
  ul.points li::before { content: ""; position: absolute; left: 2px; top: 6px;
    width: 5px; height: 5px; border-radius: 50%; background: var(--text); }
  ul.points li.note { padding-left: 16px; }
  ul.points li.note::before { display: none; }

  .pace-band { left: 800px; top: 289px; width: 400px; height: 53px; background: var(--band-grey);
    padding: 6px 0 0 35px; font-weight: 700; font-size: 14.5px; line-height: 1.25; color: #222; }

  .quote-box { left: 800px; top: 623px; width: 400px; height: 226px; background: var(--quote-violet); color: var(--white); }
  .quote-box .mark { position: absolute; font-size: 40px; font-weight: 700; line-height: 1; }
  .quote-box .mark.open { left: 32px; top: 18px; }
  .quote-box .mark.close { left: 96px; top: 168px; }
  .quote-box p { position: absolute; left: 32px; top: 54px; width: 345px;
    font-style: italic; font-weight: 600; font-size: 12px; line-height: 1.5; }
</style>
</head>
<body>
<div class="spread">

  <div class="abs photo-family-beach" role="img" aria-label="Photo of a father hugging two young children on a beach by the sea"></div>
  <div class="abs photo-beach-wash" role="img" aria-label="Faded photo of a shoreline with gentle waves and a woman walking along the sand"></div>

  <section class="abs tagline-block">
    <div class="rule top"></div>
    <p class="tagline">Helping you move through this major life challenge<br>so you can more successfully start living<br>your new life – your way!</p>
    <div class="rule bottom"></div>
  </section>

  <!-- Stage 3 -->
  <div class="abs stage-num" style="left:800px; top:0; height:93px; font-size:18px; padding-top:34px;">3</div>
  <h2 class="abs stage-title" style="left:852px; top:36px; width:330px;">The Moving On Stage – one or two coaching sessions</h2>
  <div class="abs body-copy" style="left:852px; top:100px; width:325px;">
    <p>Dealing with endings and focusing on the future:</p>
    <ul class="points" style="margin-top:2px;">
      <li>changing your “self” image and building self worth</li>
      <li>transitioning from married life to being single again</li>
      <li>address barriers preventing you form moving forward</li>
      <li>setting realistic goals to help transition to your new life more effectively</li>
    </ul>
  </div>

  <div class="abs pace-band">Everyone is different and moves through<br>the stages at their own pace.</div>
  <div class="abs photo-mother-son" role="img" aria-label="Photo of a smiling mother hugging her young son in tall green grass"></div>

  <section class="abs quote-box">
    <span class="mark open">“</span>
    <p>Often family and friends can try to influence decisions based on what they see as best, so you can feel under an enormous pressure to keep them happy. Coaching offers an objective and neutral sounding board there just for you.</p>
    <span class="mark close">”</span>
  </section>

  <!-- Left panel stages -->
  <p class="abs body-copy" style="left:50px; top:297px;">You will go through distinct stages:</p>

  <div class="abs stage-num" style="left:0; top:325px; height:77px;">1.</div>
  <h2 class="abs stage-title" style="left:47px; top:326px; width:300px;">The Preparation Stage –<br>maybe entail one or<br>two coaching sessions</h2>
  <div class="abs body-copy" style="left:47px; top:414px; width:330px;">
    <p>Anticipating all the unknowns and preparing before you see a Family Law Solicitor can save a lot of your solicitor’s time and therefore money. The clearer you are on what you want to achieve throughout the process, the more specific legal advice you will receive.</p>
  </div>

  <div class="abs stage-num" style="left:0; top:521px; height:77px;">2.</div>
  <h2 class="abs stage-title" style="left:47px; top:533px; width:320px;">The Business Side of Divorce –<br>maybe two to four coaching sessions</h2>
  <div class="abs body-copy" style="left:47px; top:598px; width:335px;">
    <p>Divorce involves multiple areas of change, intensity of emotions, life changing decisions, loss of family structure and often a sense of isolation not experienced before. Necessary</p>
    <p>The emotional overwhelm associated with relationship breakdown and the associated loss of 24/7 contact with children can impact even the most together person’s ability to make well considered decisions.</p>
    <p>Together, we will process emotions constructively and clarify decisions to be made… for you to be better able to communicate these in negotiations as well as set new boundaries.</p>
  </div>

  <!-- Middle panel skills -->
  <div class="abs body-copy" style="left:437px; top:322px; width:335px;">
    <p>Where necessary we can work on skills you will need for successful outcomes with property settlements and parenting orders e.g.</p>
    <ul class="points" style="margin-top:14px;">
      <li>conflict resolution skills plus specific verbal &amp; written communication skills important for more neutral emails and messages</li>
      <li>having difficult conversations</li>
      <li>preparing before attending joint conferences or mediation</li>
      <li>managing anger</li>
      <li>supporting your children to also navigate changed family structures</li>
      <li>strategies for you to start healing and become whole again</li>
      <li>drafting a parenting plan to anticipate &amp; address possible parenting issues, leading to more positive and successful co-parenting in the long term.</li>
      <li class="note">This is in everyone’s interests… especially your children’s.</li>
      <li>grieving losses … even if you are the one who made the decision to leave</li>
      <li>look at possible stress strategies to sustain your energy levels, important for you to make good considered decisions</li>
    </ul>
  </div>

  <div class="abs fold" style="left:399px;"></div>
  <div class="abs fold" style="left:800px;"></div>
</div>
</body>
</html>
```